Hi, Looking for an upgraded business card to the aged one attached. Open to suggestions and no real limitations, but if your going to use a picture of a taxi i think it should be vector based rather than a full color picture. I've uploaded a 2 pictures of the type of taxi which is a Torvane K5 in white. The taxi markings look like the pink one in the picture but to be clear his is white. The taxi is in Bermuda so if you wanted to include something island based that's ok as well but not required. The other thing he wanted to keep on there was the Harbour Watch, with the retired police office incorporated somehow.

Requirements
Must have
• Bermuda Taxi Operator
Retired Police Officer
Police Crest
Taxi #
Email
Mobile Number

```html
<!DOCTYPE html>
<html lang="en">
<head>
<meta charset="utf-8">
<title>Bermuda Taxi Operator – Business Card</title>
<link rel="stylesheet" href="https://fonts.googleapis.com/css2?family=Arimo:wght@400;700&family=Roboto+Condensed:wght@700&display=swap">
<style>
  :root {
    --navy: #064a82;
    --navy-deep: #053f70;
    --paper: #ffffff;
    --stage: #dcdcdc;
    --ink: #2a2a2a;
    --rule: #9a9a9a;
    --van-light: #f1f1f1;
    --van-mid: #dedede;
  }
  * { box-sizing: border-box; margin: 0; padding: 0; }
  html, body { width: 1200px; height: 900px; overflow: hidden; background: var(--stage); }
  .stage { position: relative; width: 1200px; height: 900px; }

  .card {
    position: absolute;
    width: 665px;
    height: 380px;
    border-radius: 30px;
    overflow: hidden;
    box-shadow: 0 6px 18px rgba(0,0,0,0.12);
  }

  /* Back side */
  .card-back { left: 110px; top: 40px; background: var(--navy); }
  .card-back .title {
    position: absolute; left: 0; right: 0; top: 160px;
    text-align: center;
    font-family: "Roboto Condensed", "Arial Narrow", sans-serif;
    font-weight: 700; font-size: 44px; letter-spacing: 1.5px;
    color: var(--paper);
  }

  /* Front side */
  .card-front { left: 425px; top: 470px; background: var(--paper); }
  .card-front .band {
    position: absolute; left: 0; right: 0; top: 78px; height: 46px;
    background: var(--navy);
  }
  .card-front .vehicle-art {
    position: absolute; left: 300px; top: 130px; width: 365px; height: 250px;
    border-radius: 60px 30px 0 0;
    background: linear-gradient(160deg, var(--van-light) 0%, var(--van-mid) 100%);
    opacity: 0.7;
  }
  .card-front .crest-disc {
    position: absolute; left: 232px; top: 26px; width: 150px; height: 150px;
    border-radius: 50%; background: var(--paper);
    display: flex; align-items: center; justify-content: center; text-align: center;
  }
  .card-front .crest-name {
    font-family: "Arimo", Arial, sans-serif; font-weight: 700;
    font-size: 17px; line-height: 1.2; color: var(--navy);
  }
  .card-front .details {
    position: absolute; left: 200px; top: 178px; width: 300px;
    font-family: "Arimo", Arial, sans-serif; text-align: center; color: var(--ink);
  }
  .details .name { font-weight: 700; font-size: 30px; letter-spacing: 0.5px; color: var(--navy); }
  .details .role { font-size: 17px; margin-top: 2px; }
  .details .divider { width: 170px; height: 1px; background: var(--rule); margin: 10px auto 8px; }
  .details .taxi-no, .details .email { font-size: 16px; line-height: 1.45; }
  .details .phone { font-weight: 700; font-size: 30px; color: var(--navy); margin-top: 6px; }
</style>
</head>
<body>
<main class="stage">
  <section class="card card-back" aria-label="Card back">
    <h1 class="title">BERMUDA TAXI OPERATOR</h1>
  </section>

  <section class="card card-front" aria-label="Card front">
    <div class="band"></div>
    <div class="vehicle-art" role="img" aria-label="Faint vector outline of a white Torvane K5 taxi van"></div>
    <div class="crest-disc">
      <span class="crest-name">HARBOUR<br>WATCH</span>
    </div>
    <div class="details">
      <p class="name">DALTON MERIDE</p>
      <p class="role">Retired Police Officer</p>
      <div class="divider"></div>
      <p class="taxi-no">Taxi# T2407</p>
      <p class="email">dmeride166@harbourmail.com</p>
      <p class="phone">1-441-555-0148</p>
    </div>
  </section>
</main>
</body>
</html>
```